Packaging design for HOT NEW RETAIL BEARD OIL BRAND - Merrow Fennick Apothecary

Packaging design for beard oils. I've attached a brief, and I've also attached a few examples of bottles and boxes. Of course, we need an entirely unique look. I've attached the photo of Merrow Fennick as well - you can choose to use it or not (I'm open).

This product will be sold at national retailers and needs to look like a brand that is sold at boutique

What the consumer wants to see on the shelf:
-Box should larger than others and be soft touch (feels luxurious)
-More “hipster look/feel”
-Text should stand out like inspiration photos - jumping off the shelf to the consumer
-Use the existing logo of Merrow Fennick
-Deco will be wrap label as shown in current product image
-Sample text to pull copy for outer carton (taken from label on glass bottle):
-Strengthen and condition your beard with this blend of natural oils. Sunflower oil is rich in omega, fatty acids and vitamins E, C, B, and A, while avocado oil hydrates the beard fibers from root to tip, keep the beard looking and feeling extraordinary. Smooth into your beard for a healthy sheen and a woodsy scent evoking the great outdoors.
-Cool/Hipster product at discount pricing

Target Market(s)

Men from ages 20-40. Women also buy this product for their men, so it needs to look like a well known brand.

Industry/Entity Type

Hair And Beauty

Font styles to use
Sans Serif

Colors

Designer to choose colors to be used in the design.

Requirements
Must have
• A full label and box design with key call outs:
• Features and benefits - found in attached brief
• Description of what it is: Beard Oil
• Name of frangrance: Sandalwood
• Size: 2 oz / 60 ml
Nice to have
• Feel free to revamp the logo if needed. I am not married to the font for Merrow Fennick Apothecary.

```html
<!DOCTYPE html>
<html lang="en">
<head>
<meta charset="utf-8">
<title>Merrow Fennick Apothecary – Sandalwood Beard Oil Packaging</title>
<link rel="stylesheet" href="https://fonts.googleapis.com/css2?family=Oswald:wght@500;600&family=Josefin+Sans:wght@300;400&family=Rajdhani:wght@500&display=swap">
<style>
  :root{
    --bg:#dcdde0;
    --ink:#0d0d0d;
    --panel:#111111;
    --panel-edge:#1c1c1c;
    --silver-text:#e8e8e8;
    --rule:#bdbdbd;
    --band:linear-gradient(90deg,#8e8e8e 0%,#e6e6e6 28%,#cfcfcf 62%,#8a8a8a 100%);
    --portrait:radial-gradient(ellipse at 50% 40%,#8d8d8d 0%,#4a4a4a 45%,#1d1d1d 80%,#151515 100%);
    --body-text:#2a2a2a;
  }
  *{box-sizing:border-box;margin:0;padding:0}
  html,body{width:1200px;height:1200px;overflow:hidden;background:var(--bg)}
  .canvas{position:relative;width:1200px;height:1200px}

  /* ---------- carton ---------- */
  .carton-side{position:absolute;left:60px;top:125px;width:280px;height:950px;background:var(--panel-edge);
    display:flex;align-items:center;justify-content:center}
  .carton-side__title{writing-mode:vertical-rl;font-family:"Josefin Sans",sans-serif;font-weight:300;
    font-size:66px;letter-spacing:12px;color:var(--silver-text);white-space:nowrap}

  .carton-front{position:absolute;left:340px;top:125px;width:310px;height:950px;background:var(--panel);
    color:var(--silver-text);overflow:hidden}

  .crest{position:absolute;left:0;right:0;display:flex;align-items:center;gap:10px;padding:0 10px}
  .crest__rule{flex:1;height:1px;background:var(--rule)}
  .crest__mark{width:12px;height:12px;border:1px solid var(--rule)}

  .scent{position:absolute;left:0;right:0;text-align:center;font-family:"Josefin Sans",sans-serif;font-weight:300;color:var(--silver-text);white-space:nowrap}
  .name{position:absolute;left:0;right:0;text-align:center;font-family:"Oswald",sans-serif;font-weight:600;
    color:var(--silver-text);line-height:1;text-transform:uppercase;white-space:nowrap}
  .band{position:absolute;left:0;right:0;background:var(--band);display:flex;align-items:center;justify-content:center;
    font-family:"Oswald",sans-serif;font-weight:500;color:var(--ink);text-transform:uppercase;white-space:nowrap}
  .portrait{position:absolute;left:0;right:0;background:var(--portrait)}
  .product{position:absolute;left:0;right:0;text-align:center;font-family:"Oswald",sans-serif;font-weight:600;
    color:var(--silver-text);line-height:1;text-transform:uppercase;white-space:nowrap}
  .rule{position:absolute;height:1px;background:var(--rule)}
  .size{position:absolute;left:0;right:0;text-align:center;font-family:"Josefin Sans",sans-serif;font-weight:400;color:var(--silver-text);white-space:nowrap}
  .social{position:absolute;left:0;right:0;display:flex;justify-content:center;gap:4px}
  .social span{width:11px;height:11px;border-radius:50%;background:var(--silver-text)}

  .carton-front .crest{top:32px}
  .carton-front .scent{top:68px;font-size:22px;letter-spacing:4px}
  .carton-front .name--first{top:114px;font-size:78px}
  .carton-front .name--last{top:204px;font-size:54px;letter-spacing:6px}
  .carton-front .band{top:282px;height:57px;font-size:31px;letter-spacing:3px}
  .carton-front .portrait{top:339px;height:460px}
  .carton-front .product{top:748px;font-size:40px}
  .carton-front .rule{left:6px;right:6px;top:799px}
  .description{position:absolute;left:0;right:0;top:806px;height:82px;background:var(--band);padding:6px 10px;
    font-family:"Rajdhani",sans-serif;font-weight:500;font-size:8.6px;line-height:1.3;color:var(--body-text);text-align:center}
  .carton-front .size{top:900px;font-size:16px}
  .carton-front .social{top:926px}

  /* ---------- bottle wrap label ---------- */
  .label{position:absolute;left:710px;top:240px;width:430px;height:720px;background:var(--panel);display:flex}
  .label__face{position:relative;width:360px;height:100%;overflow:hidden}
  .label__face .crest{top:28px;padding:0 40px}
  .label__face .scent{top:58px;font-size:17px;letter-spacing:3px}
  .label__face .name--first{top:94px;font-size:68px}
  .label__face .name--last{top:172px;font-size:46px;letter-spacing:5px}
  .label__face .band{top:236px;left:30px;right:30px;height:46px;font-size:26px;letter-spacing:3px}
  .label__face .portrait{top:282px;left:30px;right:30px;height:370px}
  .label__face .product{top:602px;font-size:40px}
  .label__face .rule{left:30px;right:30px;top:652px}
  .label__face .size{top:668px;font-size:15px}

  .label__copy{position:relative;width:70px;height:100%;padding:40px 8px 60px}
  .label__copy-strip{height:100%;background:var(--band);display:flex;align-items:center;justify-content:center;padding:6px 2px}
  .label__copy-text{writing-mode:vertical-rl;font-family:"Rajdhani",sans-serif;font-weight:500;font-size:7.4px;
    line-height:1.25;color:var(--body-text);max-height:100%}
  .label__copy .social{top:auto;bottom:28px}
</style>
</head>
<body>
<main class="canvas">

  <section class="carton-side" aria-label="Carton side panel">
    <p class="carton-side__title">MEN'S BEARD OIL</p>
  </section>

  <section class="carton-front" aria-label="Carton front panel">
    <div class="crest"><span class="crest__rule"></span><span class="crest__mark"></span><span class="crest__rule"></span></div>
    <p class="scent">SANDALWOOD</p>
    <h1 class="name name--first">Merrow</h1>
    <p class="name name--last">Fennick</p>
    <div class="band">-Apothecary-</div>
    <div class="portrait" role="img" aria-label="Black and white vintage portrait of Merrow Fennick"></div>
    <h2 class="product">Men's Beard Oil</h2>
    <div class="rule"></div>
    <p class="description">Strengthen and condition your beard with this blend of natural oils. Sunflower oil is rich in omega, fatty acids and vitamins E, C, B, and A, while avocado oil hydrates the beard fibers from root to tip, keep the beard looking and feeling extraordinary. Smooth into your beard for a healthy sheen and a woodsy scent evoking the great outdoors.</p>
    <p class="size">2 fl Oz. / 60ml</p>
    <div class="social" aria-hidden="true"><span></span><span></span><span></span></div>
  </section>

  <section class="label" aria-label="Bottle wrap label">
    <div class="label__face">
      <div class="crest"><span class="crest__rule"></span><span class="crest__mark"></span><span class="crest__rule"></span></div>
      <p class="scent">SANDALWOOD</p>
      <p class="name name--first">Merrow</p>
      <p class="name name--last">Fennick</p>
      <div class="band">-Apothecary-</div>
      <div class="portrait" role="img" aria-label="Black and white vintage portrait of Merrow Fennick"></div>
      <p class="product">Men's Beard Oil</p>
      <div class="rule"></div>
      <p class="size">2 fl Oz. / 60ml</p>
    </div>
    <div class="label__copy">
      <div class="label__copy-strip">
        <p class="label__copy-text">Strengthen and condition your beard with this blend of natural oils. Sunflower oil is rich in omega, fatty acids and vitamins E, C, B, and A, while avocado oil hydrates the beard fibers from root to tip, keep the beard looking and feeling extraordinary. Smooth into your beard for a healthy sheen and a woodsy scent evoking the great outdoors.</p>
      </div>
      <div class="social" aria-hidden="true"><span></span><span></span></div>
    </div>
  </section>

</main>
</body>
</html>
```